Brighten Every Calling book cover and updated company logo bundle

USE THE LOGO ON THE BACK COVER. I WANT AN UPDATED LOOK TO MY LOGO
Size of book: 5.5 x 8.5
Title: Brighten Every Calling
Subtitle: An introvert’s guide to creating a coaching business that reflects who you are
The Subtitle does NOT go on the book cover
Author: Marla Toppington
BOOK DESCRIPTION: This book will help coaches and creative professionals get confidently clear on who they are so they can create a business that reflects their inner message.

DEMOGRAPHICS — Coaches and creative professional age 35-45

WOULD YOU PREFER PEOPLE OR OBJECTS ON YOUR COVER?
Objects or abstract designs
Anything I don’t want on the cover? people
Objects or symbols I want on the cover: possibly magnifying glass

IF YOU HAVE ANY PHOTOS THAT YOU WOULD LIKE US TO USE, PLEASE INCLUDE THE LINK(S) HERE. My logo or face pic for the back cover (Face pic pending)

COPY FOR THE SPINE
Brighten Every Calling
Marla Toppington
Lanternhall Books (with logo)

COPY FOR THE BACK COVER (270 words) my biz logo at the bottom and my picture next to my short bio. (Picture to come)

Create a Coaching Business that Reflects Who You Are

Do you want to step confidently into your new career by doing what you love? You aren't alone! But instead of doing what they love, many new coaches get stuck by trying to fit into traditional ways of doing business and create many unnecessary hurdles to happiness and success.
In this book, creative business coach, Marla Toppington teaches you, as she has taught herself and many others, to stop feeling guilty about what you “should” do in your life and in the process you will learn how to turn your passion into a purposeful career.

New coaches will learn how to:
• Recognize how your life decisions to this point are holding you back.
• Discover your gifts so you can express yourself through your creative projects.
• Identify and develop tools to bring your passion into purpose
• Offer services based on what you love to do.
• Understand your personal work style and work-flow to optimize your ideas and productivity.
• Create a message that reflects who you are to attract clients to work with you.
• Ask confidently for what you are worth and get it every time.
Join Marla on the journey of reconnecting with yourself and manifesting your dream.

Marla Toppington, founder of Quiet Harbor Wellness, helps new coaches and creative entrepreneurs find their inner voice so that they have the confidence to bring their authentic selves out into the world. Marla has gone through this process for herself and helped other new businesses achieve dramatic improvements in their organization and focus as a result.

Target Market(s)

indicated in description

Industry/Entity Type

Life Coaching

Logo Text

Quiet Harbor Wellness

Requirements
Must have
• updated look on existing logo it is going on the back of the book
Nice to have
• I like the font in the book cover I attached but Id like to see what else is possible

```html
<!DOCTYPE html>
<html lang="en">
<head>
<meta charset="utf-8">
<title>Brighten Every Calling — Book Cover</title>
<link rel="stylesheet" href="https://fonts.googleapis.com/css2?family=Montserrat:wght@700;800&family=Source+Sans+3:wght@300;400;600&family=Shadows+Into+Light&display=swap">
<style>
  :root {
    --paper: #dcdfe5;
    --ink: #111111;
    --accent-red: #b8434a;
    --accent-orange: #e0711e;
    --rule-red: #b02a2a;
    --photo-box: #050505;
    --code-box: #1f1f1f;
    --logo-ink: #d9741f;
  }
  html, body {
    margin: 0;
    padding: 0;
    overflow: hidden;
    background: var(--paper);
  }
  .cover {
    position: relative;
    width: 1200px;
    height: 903px;
    background: var(--paper);
    overflow: hidden;
    font-family: "Source Sans 3", "Source Sans Pro", sans-serif;
    color: var(--ink);
  }

  /* Back cover */
  .back-heading {
    position: absolute;
    left: 40px;
    top: 36px;
    width: 522px;
    margin: 0;
    text-align: center;
    font-weight: 600;
    font-size: 32px;
    line-height: 34px;
    color: var(--accent-red);
    letter-spacing: -0.2px;
  }
  .back-copy {
    position: absolute;
    left: 60px;
    top: 110px;
    width: 483px;
    font-size: 14.6px;
    line-height: 20px;
    text-align: justify;
  }
  .back-copy p { margin: 0; }
  .back-copy .lead,
  .back-copy .list-intro { color: var(--accent-orange); }
  .benefits {
    list-style: none;
    margin: 0;
    padding: 0;
  }
  .benefits li::before {
    content: "•";
    margin-right: 6px;
  }
  .back-rule {
    position: absolute;
    left: 116px;
    top: 551px;
    width: 372px;
    height: 3px;
    background: radial-gradient(ellipse at center, var(--rule-red) 55%, transparent 100%);
    border-radius: 50%;
  }
  .author-photo {
    position: absolute;
    left: 59px;
    top: 568px;
    width: 142px;
    height: 150px;
    background: var(--photo-box);
  }
  .author-bio {
    position: absolute;
    left: 207px;
    top: 567px;
    width: 341px;
    margin: 0;
    font-size: 15.4px;
    line-height: 18.6px;
    text-align: justify;
  }
  .brand-mark {
    position: absolute;
    left: 90px;
    top: 780px;
    display: flex;
    align-items: center;
    gap: 10px;
  }
  .brand-mark .dot {
    width: 40px;
    height: 40px;
    border-radius: 50%;
    background: var(--logo-ink);
  }
  .brand-mark .name {
    width: 160px;
    font-weight: 600;
    font-size: 19px;
    line-height: 21px;
    color: var(--logo-ink);
  }
  .code-area {
    position: absolute;
    left: 346px;
    top: 742px;
    width: 210px;
    height: 122px;
    background: var(--code-box);
  }

  /* Spine */
  .spine-text {
    position: absolute;
    left: 586px;
    white-space: nowrap;
    writing-mode: vertical-rl;
  }
  .spine-title { top: 144px; font-weight: 600; font-size: 17.5px; letter-spacing: 0.1px; }
  .spine-author { top: 410px; font-weight: 400; font-size: 21px; }
  .spine-publisher { top: 660px; font-weight: 600; font-size: 11.5px; left: 592px; }

  /* Front cover */
  .front-title {
    position: absolute;
    left: 660px;
    top: 52px;
  }
  .front-title .main {
    font-family: "Montserrat", sans-serif;
    font-weight: 800;
    font-size: 112px;
    fill: var(--ink);
  }
  .front-subtitle {
    position: absolute;
    left: 716px;
    top: 168px;
    margin: 0;
    font-family: "Shadows Into Light", cursive;
    font-size: 74px;
    line-height: 74px;
    color: var(--accent-red);
    transform: rotate(-11deg);
    transform-origin: left center;
    white-space: nowrap;
  }
  .cover-art {
    position: absolute;
    left: 704px;
    top: 276px;
    width: 412px;
    height: 436px;
    border-radius: 40% 40% 45% 20%;
    background: radial-gradient(circle at 62% 40%, rgba(90, 84, 80, 0.35), rgba(120, 110, 100, 0.22) 55%, rgba(220, 223, 229, 0) 75%);
  }
  .front-author {
    position: absolute;
    left: 740px;
    top: 772px;
    margin: 0;
    font-weight: 300;
    font-size: 46px;
    letter-spacing: -0.6px;
    white-space: nowrap;
  }
</style>
</head>
<body>
<main class="cover">

  <!-- Back cover -->
  <h2 class="back-heading">CREATE A COACHING BUSINESS<br>THAT REFLECTS WHO YOU ARE</h2>

  <div class="back-copy">
    <p><span class="lead">Do you want to step confidently into your new career</span> by doing what you love? You aren't alone! But instead of doing what they love, many new coaches get stuck by trying to fit into traditional ways of doing business and create many unnecessary hurdles to happiness and success.</p>
    <p>In this book, creative business coach, Marla Toppington teaches you, as she has taught herself and many others, to stop feeling guilty about what you “should” do in your life and in the process you will learn how to turn your passion into a purposeful career.</p>
    <p class="list-intro">New coaches will learn how to:</p>
    <ul class="benefits">
      <li>Recognize how your life decisions to this point are holding you back.</li>
      <li>Discover your gifts so you can express yourself through your creative projects.</li>
      <li>Identify and develop tools to bring your passion into purpose</li>
      <li>Offer services based on what you love to do.</li>
      <li>Understand your personal work style and work-flow to optimize your ideas and productivity.</li>
      <li>Create a message that reflects who you are to attract clients to work with you.</li>
      <li>Ask confidently for what you are worth and get it every time.</li>
    </ul>
    <p>Join Marla on the journey of reconnecting with yourself and manifesting your dream.</p>
  </div>

  <div class="back-rule"></div>

  <div class="author-photo" role="img" aria-label="Author portrait placeholder"></div>
  <p class="author-bio">Marla Toppington, founder of Quiet Harbor Wellness, helps new coaches and creative entrepreneurs find their inner voice so that they have the confidence to bring their authentic selves out into the world. Marla has gone through this process for herself and helped other new businesses achieve dramatic improvements in their organization and focus as a result.</p>

  <div class="brand-mark">
    <span class="dot"></span>
    <span class="name">Quiet Harbor Wellness</span>
  </div>

  <div class="code-area"></div>

  <!-- Spine -->
  <div class="spine-text spine-title">BRIGHTEN EVERY CALLING</div>
  <div class="spine-text spine-author">Marla Toppington</div>
  <div class="spine-text spine-publisher">Lanternhall Books</div>

  <!-- Front cover -->
  <svg class="front-title" width="500" height="110" viewBox="0 0 500 110" aria-label="Brighten">
    <text class="main" x="2" y="98" textLength="492" lengthAdjust="spacingAndGlyphs">BRIGHTEN</text>
  </svg>
  <h1 class="front-subtitle">every calling</h1>

  <div class="cover-art" role="img" aria-label="Crowd of small figures arranged in the shape of a magnifying glass"></div>

  <p class="front-author">Marla Toppington</p>
</main>
</body>
</html>
```